Web Design Project (uncoded)

About Us
ZumLink is a telecom startup and is looking to launch its website.
ZumLink specializes in providing communication solutions to the travel market. Our mission is to develop cost effective communication products and solutions for the international traveler.
Our simple vision of "every hotel should have a mobile phone in the guest rooms", led us to develop a pathbreaking & cost effective mobile phone. With full integration capabilities with the hotels property management system, location based marketing, user locator and other features, this product is unique in addressing the hospitality segment.
The website is targeted at hotel owners and property management companies.
The website should have a young contemporary and a funky look, in line with the name.
Please find attached our logo (for the colors etc.). (attached now).
We would like to receive the design for a home page and an inside page for the website.
Site map would be as follows: Home, About Us, Solutions, Contact us
Thanks and look forward,
Tamsa
Target Market(s)
Hotel decision makers
Industry/Entity Type
Property Management
Look and feel
Each slider illustrates characteristics of the customer's brand and the style your logo design should communicate.

```html
<!DOCTYPE html>
<html lang="en">
<head>
<meta charset="utf-8">
<title>ZumLink – Home</title>
<link rel="stylesheet" href="https://fonts.googleapis.com/css2?family=Signika:wght@400;600&family=Arimo:wght@400;700&display=swap">
<style>
:root{
  --orange:#f08c00;
  --orange-soft:#f5a623;
  --ink:#333;
  --ink-soft:#555;
  --page:#ebebeb;
  --panel:#d9d9d9;
  --white:#fff;
  --footer-light:#eeeeee;
  --footer-dark:#2b2b2b;
  --grey-icon:#8a8a8a;
}
*{box-sizing:border-box;margin:0;padding:0}
html,body{width:880px;height:1200px;overflow:hidden}
body{position:relative;background:var(--page);font-family:"Arimo",Arial,sans-serif;color:var(--ink)}
.abs{position:absolute}
.top-bar{left:0;top:0;width:880px;height:3px;background:var(--orange)}

/* header */
.brand{left:48px;top:24px;display:flex;align-items:center;gap:10px}
.brand-mark{width:77px;height:77px;border-radius:50%;background:var(--orange)}
.brand-name{font-family:"Signika",sans-serif;font-weight:600;font-size:40px;color:#222;letter-spacing:-1px}
.connect{left:608px;top:19px;display:flex;align-items:center;gap:4px}
.connect-label{font-family:"Signika",sans-serif;font-weight:600;font-size:15px;color:#666;margin-right:5px}
.connect-dot{width:19px;height:19px;border-radius:50%;background:var(--grey-icon)}
.main-nav{left:470px;top:93px;display:flex;gap:6px}
.nav-item{display:flex;align-items:center;gap:6px;height:26px;padding:0 6px 0 6px;border-radius:13px;background:linear-gradient(to right,transparent,#dcdcdc);font-family:"Signika",sans-serif;font-size:12px;font-weight:600;color:#444}
.nav-item.is-active{color:var(--orange)}
.nav-caret{width:12px;height:12px;border-radius:50%;background:#fff;box-shadow:0 1px 2px rgba(0,0,0,.3);display:flex;align-items:center;justify-content:center}

/* hero */
.hero-panel{left:46px;top:138px;width:792px;height:356px;background:var(--panel);clip-path:polygon(0 0,100% 0,99% 50%,100% 100%,0 100%,1% 50%)}
.hero-frame{left:54px;top:152px;width:775px;height:326px;background:var(--white);box-shadow:0 1px 4px rgba(0,0,0,.2)}
.hero-photo{left:64px;top:160px;width:758px;height:314px;background:linear-gradient(90deg,#3a2a22 0%,#5a4438 35%,#c9c2ba 55%,#e8e4df 100%)}

/* intro */
.section-title{font-family:"Signika",sans-serif;font-weight:600;font-size:18px}
.intro-title{left:56px;top:528px;color:var(--orange)}
.intro-text{left:56px;top:566px;width:324px;font-size:9.6px;line-height:14.4px;color:var(--ink-soft);text-align:justify}
.intro-list{left:56px;top:636px;width:336px;list-style:none;font-size:9.6px;line-height:14.4px;color:var(--ink-soft)}
.intro-list li{position:relative;padding-left:15px;margin-bottom:5px}
.intro-list li::before{content:"»";position:absolute;left:0;top:-1px;color:#e04a00;font-weight:700;font-size:12px}
.view-more{left:300px;top:736px;width:84px;text-align:right;font-family:"Signika",sans-serif;font-weight:600;font-size:12px;color:var(--orange)}
.col-divider{left:392px;top:540px;width:1px;height:208px;background:#c9c9c9}

/* videos */
.video-icon{left:409px;top:527px;width:26px;height:26px;border-radius:50%;background:var(--orange);border:3px solid #ddd}
.video-title{left:444px;top:527px;color:#333}
.see-all{left:730px;top:528px;width:64px;height:22px;border-radius:11px;background:var(--orange-soft);color:#fff;font-family:"Signika",sans-serif;font-weight:600;font-size:11px;display:flex;align-items:center;justify-content:center}
.video-card{top:580px;width:204px;height:126px;background:var(--white);padding:2px;box-shadow:0 1px 3px rgba(0,0,0,.25)}
.video-card .thumb{width:100%;height:100%}
.video-one{left:407px}
.video-one .thumb{background:linear-gradient(180deg,#444,#9a9a9a 50%,#333)}
.video-two{left:620px}
.video-two .thumb{background:linear-gradient(180deg,#fafafa,#e6e6e6 80%,#222 80%)}
.video-count{left:409px;top:724px;width:53px;height:16px;background:var(--orange-soft);border-radius:2px;color:#fff;font-size:8.5px;display:flex;align-items:center;justify-content:center}
.pager{top:719px;width:20px;height:19px;background:var(--white);border-radius:3px;box-shadow:0 1px 2px rgba(0,0,0,.3);display:flex;align-items:center;justify-content:center}

/* projects */
.rule{left:50px;top:772px;width:768px;height:1px;background:#c9c9c9}
.projects-icon{left:62px;top:782px;width:32px;height:36px;background:#f4f4f4;box-shadow:0 1px 3px rgba(0,0,0,.25)}
.projects-icon::after{content:"";position:absolute;left:10px;top:14px;width:22px;height:22px;border-radius:50%;background:#c44b6a}
.projects-title{left:104px;top:789px;color:#333}
.project{top:828px;width:166px;height:122px;background:var(--white);padding:5px;box-shadow:0 6px 6px -4px rgba(0,0,0,.35)}
.project .thumb{width:100%;height:100%}
.thumb-meeting{background:linear-gradient(135deg,#c9a37a,#5a6a7a 60%,#e8e0d6)}
.thumb-phones{background:linear-gradient(135deg,#1e6e6a,#d88a3a 55%,#204f4d)}
.thumb-duo{background:linear-gradient(135deg,#dfe4ea,#b9775a 50%,#7b8fb5)}
.carousel-edge{top:870px;width:18px;height:46px;border:2px solid #ccc;border-radius:50%}

/* footer */
.footer-light{left:0;top:982px;width:880px;height:104px;background:var(--footer-light);border-top:1px solid #d4d4d4}
.foot-col{top:990px;font-size:10px;line-height:14.4px;color:#555}
.foot-col h4{font-family:"Signika",sans-serif;font-weight:600;font-size:11.5px;color:#333;line-height:16px}
.copyright{left:70px;top:990px;font-size:10px;color:#555;line-height:16px}
.copyright b{color:#333}
.tag-update{display:inline-block;background:var(--orange);color:#fff;font-size:6.5px;font-weight:700;padding:0 3px;line-height:9px;border-radius:1px;margin-right:3px;vertical-align:1px}
.contact b{color:#333}
.footer-dark{left:0;top:1086px;width:880px;height:114px;background:var(--footer-dark)}
.notch{left:474px;top:1086px;width:0;height:0;border-left:7px solid transparent;border-right:7px solid transparent;border-top:7px solid var(--footer-light)}
.foot-brand{left:50px;top:1110px;display:flex;align-items:center;gap:8px}
.foot-brand .brand-mark{width:64px;height:64px;background:#666;border:4px solid #999}
.foot-brand .brand-name{color:#eee;font-size:32px}
.foot-social{top:1132px;width:22px;height:22px;border-radius:2px;background:#3a7bbf}
.stay-title{left:455px;top:1103px;font-family:"Arimo",sans-serif;font-weight:700;font-size:14px;color:#fff}
.stay-text{left:455px;top:1123px;width:340px;font-size:10px;line-height:14.4px;color:#eee}
.signup{left:455px;top:1159px;display:flex;gap:4px}
.email-field{width:134px;height:22px;background:#fff;border-radius:2px;display:flex;align-items:center;font-size:10px;color:#999}
.email-field .env{width:22px;height:100%;border-right:1px solid #ccc;display:flex;align-items:center;justify-content:center}
.subscribe{width:75px;height:22px;background:#f4f4f4;border-radius:2px;font-size:10px;color:#333;display:flex;align-items:center;justify-content:center;gap:2px}
</style>
</head>
<body>
<div class="abs top-bar"></div>

<header>
  <div class="abs brand"><span class="brand-mark"></span><span class="brand-name">ZumLink</span></div>
  <div class="abs connect">
    <span class="connect-label">Connect with us</span>
    <span class="connect-dot"></span><span class="connect-dot"></span><span class="connect-dot"></span><span class="connect-dot"></span><span class="connect-dot"></span>
  </div>
  <nav class="abs main-nav">
    <span class="nav-item is-active"><span class="nav-caret"><svg width="6" height="4"><path d="M0 0h6L3 4z" fill="#333"/></svg></span>Home</span>
    <span class="nav-item"><span class="nav-caret"><svg width="6" height="4"><path d="M0 0h6L3 4z" fill="#333"/></svg></span>About Us</span>
    <span class="nav-item"><span class="nav-caret"><svg width="6" height="4"><path d="M0 0h6L3 4z" fill="#333"/></svg></span>Solutions</span>
    <span class="nav-item"><span class="nav-caret"><svg width="6" height="4"><path d="M0 0h6L3 4z" fill="#333"/></svg></span>Contact us</span>
  </nav>
</header>

<section>
  <div class="abs hero-panel"></div>
  <div class="abs hero-frame"></div>
  <div class="abs hero-photo" role="img" aria-label="Hotel café interior with chalkboard wall beside a woman on the phone at a desk"></div>
</section>

<section>
  <h2 class="abs section-title intro-title">What can we do for you?</h2>
  <p class="abs intro-text">Lorem Ipsum is simply dummy text of the printing and typesetting industry. Lorem Ipsum has been the industry's standard dummy text ever since the 1500s, when an unknown printer took a galley of type and scrambled it to make a type specimen book.</p>
  <ul class="abs intro-list">
    <li>Lorem Ipsum is simply dummy text of the printing and</li>
    <li>Lorem Ipsum is simply dummy text of the printing and typesetting industry. Lorem Ipsum has been the industry's</li>
    <li>Dummy text of the printing and typesetting industry. Lorem Ipsum has been the industry's</li>
  </ul>
  <span class="abs view-more">View more</span>
  <div class="abs col-divider"></div>

  <span class="abs video-icon"></span>
  <h2 class="abs section-title video-title">Mobile Marketing Video Series</h2>
  <span class="abs see-all">See all</span>
  <div class="abs video-card video-one"><div class="thumb" role="img" aria-label="Video still of a rich media mobile platform demo"></div></div>
  <div class="abs video-card video-two"><div class="thumb" role="img" aria-label="Video still with a mobile marketing fact and a hand holding a phone"></div></div>
  <span class="abs video-count">5 of 120</span>
  <span class="abs pager" style="left:777px"><svg width="8" height="11"><path d="M7 1L2 5.5 7 10" stroke="#333" stroke-width="2" fill="none"/></svg></span>
  <span class="abs pager" style="left:802px"><svg width="8" height="11"><path d="M1 1l5 4.5L1 10" stroke="var(--orange)" stroke-width="2" fill="none"/></svg></span>
</section>

<section>
  <div class="abs rule"></div>
  <span class="abs projects-icon"></span>
  <h2 class="abs section-title projects-title">Recent Projects</h2>
  <div class="abs carousel-edge" style="left:46px;border-right-color:transparent"></div>
  <div class="abs carousel-edge" style="left:804px;border-left-color:transparent"></div>
  <div class="abs project" style="left:80px"><div class="thumb thumb-meeting" role="img" aria-label="Two colleagues on phone calls at a desk"></div></div>
  <div class="abs project" style="left:258px"><div class="thumb thumb-phones" role="img" aria-label="Group of people holding mobile phones"></div></div>
  <div class="abs project" style="left:437px"><div class="thumb thumb-meeting" role="img" aria-label="Two colleagues on phone calls at a desk"></div></div>
  <div class="abs project" style="left:620px"><div class="thumb thumb-duo" role="img" aria-label="Two young men using phones in front of a chart"></div></div>
</section>

<footer>
  <div class="abs footer-light"></div>
  <p class="abs copyright">© <b>Company</b> 2012</p>
  <div class="abs foot-col" style="left:199px"><h4>Footer menu</h4>Home<br>Second menu<br>Third menu<br>About</div>
  <div class="abs foot-col" style="left:327px"><h4>Second</h4>Home<br><span class="tag-update">UPDATE</span>Important link<br>Third menu</div>
  <div class="abs foot-col" style="left:455px"><h4>And the last</h4>Home<br>Second menu<br>Third menu<br>About<br>Next</div>
  <div class="abs foot-col contact" style="left:647px;top:992px"><b>Phone:</b> +12 [3] 40217356<br><b>Fax:</b> +12 [3] 40217359<br><br><b>Address:</b> 48/210 Cedar Bay Road</div>

  <div class="abs footer-dark"></div>
  <div class="abs notch"></div>
  <div class="abs foot-brand"><span class="brand-mark"></span><span class="brand-name">ZumLink</span></div>
  <span class="abs foot-social" style="left:286px"></span>
  <span class="abs foot-social" style="left:320px;background:#3aa3d8"></span>
  <span class="abs foot-social" style="left:353px;background:#2a7ab0"></span>
  <h3 class="abs stay-title">Stay connected</h3>
  <p class="abs stay-text">Newsletters offering a stylish and entertaining mix of information and inspiration.</p>
  <div class="abs signup">
    <span class="email-field"><span class="env"><svg width="11" height="8"><rect width="11" height="8" fill="#444"/><path d="M0 0l5.5 4.5L11 0" stroke="#fff" fill="none"/></svg></span>&nbsp;Email</span>
    <span class="subscribe"><svg width="9" height="9"><path d="M1 4.5l2.5 2.5L8 1.5" stroke="#333" stroke-width="1.6" fill="none"/></svg>Subscribe</span>
  </div>
</footer>
</body>
</html>
```